Retail Business Needs a New Ecommerce Store Design

We need a new web design for a company called Brisk Loom and Canopy (see attached logos). We sell a range of Shade Cloth and horticultural products. We want the layout to be similar to this website http://www.wombeltarpville.com.au/
and we like the design of the shopping cart and checkout. But we don't like the text used on this site and the glare.
We also like the layout of this site http://www.temparo.com/
We really like the look and feel of this website http://www.dovemarlow.com.au/
We want a bright website. You can use any colours that work with our logo besides blue. Fonts are to be striking and visible to the older generation, and the website is to be very user friendly and easy to navigate. I have attached a word doc of all the features we would like include. Don't pay any attention to the colours I have used and in regards to layout take this as a rough guide only. We want all our major categories to be easily seen on every page. The website will be built in drupal.
Key Features of the Site:
- Message box on side of page
- Special Search Box where you can search by application and Fabric type similar to the search box found here: http://www.dovemarlow.com.au/product-search
- An area on the product page that shows what else customers bought
We need the design submitted as a psd.
Pages needed for the Site:
Home
Product Page
Product Category Page
Shopping Cart Page
Checkout Page
If you have any questions in regards to this project don't hesitate to ask.
Updates
Hey all,
Thanks for your submissions we will get back to you with some feedback in the next few days after we have a meeting.
Target Market(s)
Our main target market is mostly Males over 30.
Industry/Entity Type
Business
Number of Pages Required
5+ page
Look and feel
Each slider illustrates characteristics of the customer's brand and the style your logo design should communicate.

```html
<!DOCTYPE html>
<html lang="en">
<head>
<meta charset="utf-8">
<title>Brisk Loom and Canopy — Home</title>
<link rel="stylesheet" href="https://fonts.googleapis.com/css2?family=Open+Sans:wght@400;600;700&family=Oswald:wght@300;400;500&display=swap">
<style>
:root{
  --green:#2e9a3a;
  --green-light:#52b548;
  --green-dark:#1f7a2b;
  --brand:#1d6e3a;
  --page:#efefef;
  --card:#f3f3f3;
  --card-border:#dedede;
  --ink:#333;
  --muted:#555;
  --black:#111;
  --footer:#3a3a3a;
  --white:#fff;
}
*{box-sizing:border-box;margin:0;padding:0}
html,body{width:982px;height:1200px;overflow:hidden}
body{background:var(--page);font-family:"Open Sans",Arial,sans-serif;color:var(--ink);position:relative}
.abs{position:absolute}
.top-rule{left:0;top:0;width:982px;height:3px;background:var(--green)}

/* header */
.site-search{left:700px;top:17px;width:133px;height:29px;background:var(--white);border-radius:15px 0 0 15px;display:flex;align-items:center;padding-left:12px;font-size:11px;color:#aaa}
.site-search-btn{left:806px;top:17px;width:27px;height:29px;background:var(--green);border-radius:0 6px 6px 0;display:flex;align-items:center;justify-content:center}
.cart-btn{left:848px;top:15px;width:34px;height:34px;border-radius:50%;background:var(--green);display:flex;align-items:center;justify-content:center}
.cart-summary{left:783px;top:61px;width:151px;height:26px;background:#e2e2e2;border-radius:2px;font-size:12px;color:var(--muted);display:flex;align-items:center;justify-content:center}
.social-dot{top:93px;width:20px;height:20px;border-radius:50%}
.contact-email{left:719px;top:96px;font-family:"Oswald",sans-serif;font-size:11px;color:#444;letter-spacing:.2px}
.brand{left:68px;top:60px;display:flex;align-items:center;gap:12px}
.brand-name{font-family:"Oswald",sans-serif;font-weight:400;font-size:29px;color:var(--brand);letter-spacing:-.3px}
.brand-dot{width:40px;height:40px;border-radius:50%;background:var(--brand)}

/* navigation */
.main-nav{left:68px;top:139px;width:813px;height:46px;background:linear-gradient(var(--green-light),var(--green));border-radius:3px;display:flex}
.main-nav a{color:var(--white);text-decoration:none;font-family:Arial,sans-serif;font-size:12.5px;display:flex;align-items:center;justify-content:center;border-right:1px solid rgba(0,0,0,.15)}
.main-nav a:last-child{border-right:none}

/* filter panel */
.filter-panel{left:67px;top:195px;width:197px;height:311px;background:#e4e4e4;border-radius:3px}
.filter-head{height:51px;background:linear-gradient(#333,#000);border-radius:3px 3px 0 0;color:var(--white);font-family:"Oswald",sans-serif;font-size:19px;padding:13px 0 0 17px;letter-spacing:.5px}
.filter-label{position:absolute;left:19px;top:64px;font-size:14px;color:#444}
.filter-select{position:absolute;left:19px;width:159px;height:32px;background:var(--white);border:1px solid #d0d0d0;border-radius:2px;font-size:12px;color:#222;display:flex;align-items:center;justify-content:space-between;padding:0 10px 0 15px}
.filter-submit{position:absolute;left:18px;top:261px;width:72px;height:31px;background:var(--black);color:var(--white);font-size:11.5px;border-radius:3px;display:flex;align-items:center;justify-content:center}

/* hero */
.hero{left:275px;top:195px;width:606px;height:311px;border-radius:3px;background:linear-gradient(180deg,#f4d27a 0%,#e9d9a4 30%,#9cc256 55%,#4e8a1e 100%)}
.hero-arrow{top:445px;width:32px;height:32px;border-radius:50%;background:#111;display:flex;align-items:center;justify-content:center}

/* featured */
.section-title{left:68px;top:525px;font-family:"Oswald",sans-serif;font-size:19px;color:#333;letter-spacing:.6px}
.pager{top:525px;width:24px;height:24px;background:var(--black);display:flex;align-items:center;justify-content:center}
.product-card{width:121px;height:208px;background:var(--card);border:1px solid var(--card-border);border-radius:2px}
.product-photo{position:absolute;left:12px;top:14px;width:96px;height:96px;border-radius:4px}
.product-name{position:absolute;left:15px;top:118px;font-size:12px;font-weight:700;color:#4a4a4a;line-height:15px;width:96px}
.add-cart{position:absolute;left:16px;top:166px;width:72px;height:24px;background:var(--black);color:var(--white);font-size:11px;border-radius:3px;display:flex;align-items:center;justify-content:center}

.contact-tab{left:947px;top:509px;width:35px;height:181px;background:linear-gradient(var(--green-light),var(--green-dark));border-radius:3px 0 0 3px;display:flex;align-items:center;justify-content:center}
.contact-tab span{transform:rotate(-90deg);color:var(--white);font-weight:700;font-size:13px;white-space:nowrap}

/* footer */
.site-footer{left:0;top:1070px;width:982px;height:130px;background:var(--footer)}
.footer-links{position:absolute;top:22px;left:0;width:982px;display:flex;justify-content:center;font-family:"Oswald",sans-serif;font-weight:300;font-size:11.5px;color:var(--white)}
.footer-links span{padding:0 15px;border-left:1px solid var(--white);line-height:12px}
.footer-links span:first-child{border-left:none}
.footer-social{position:absolute;top:49px;left:0;width:982px;display:flex;justify-content:center;gap:1px}
.footer-social i{width:36px;height:36px;border-radius:50%;background:#5a5a5a;display:block}
.copyright{position:absolute;top:101px;width:982px;text-align:center;font-family:"Oswald",sans-serif;font-weight:300;font-size:11px;color:var(--white)}
</style>
</head>
<body>
<div class="abs top-rule"></div>

<header>
  <div class="abs brand"><span class="brand-name">Brisk Loom and Canopy</span><span class="brand-dot"></span></div>
  <div class="abs site-search">Search</div>
  <div class="abs site-search-btn"><svg width="14" height="14" viewBox="0 0 14 14"><circle cx="6" cy="6" r="4" fill="none" stroke="#fff" stroke-width="2"/><line x1="9" y1="9" x2="13" y2="13" stroke="#fff" stroke-width="2.2"/></svg></div>
  <div class="abs cart-btn"><svg width="18" height="16" viewBox="0 0 18 16"><path d="M1 2h3l2 8h9l2-6H5" fill="none" stroke="#fff" stroke-width="1.8"/><circle cx="7" cy="13.5" r="1.5" fill="#fff"/><circle cx="14" cy="13.5" r="1.5" fill="#fff"/></svg></div>
  <div class="abs cart-summary">Shopping Cart&nbsp;&nbsp;0 Items</div>
  <span class="abs social-dot" style="left:598px;background:#3ab4e8"></span>
  <span class="abs social-dot" style="left:627px;background:#3b5a99"></span>
  <span class="abs social-dot" style="left:655px;background:#d2352a"></span>
  <span class="abs social-dot" style="left:683px;background:#e8558a"></span>
  <div class="abs contact-email">SALES@BRISKLOOMCANOPY.COM.AU</div>
</header>

<nav class="abs main-nav">
  <a style="width:68px">Home</a>
  <a style="width:90px">Shadecloth</a>
  <a style="width:131px">Greenhouse Film</a>
  <a style="width:107px">Specialty Nets</a>
  <a style="width:85px">Weedmat</a>
  <a style="width:91px">Polythene</a>
  <a style="width:84px">Windbreak</a>
  <a style="width:66px">Nails</a>
  <a style="width:91px">Accessories</a>
</nav>

<aside class="abs filter-panel">
  <div class="filter-head">SEARCH PRODUCT</div>
  <div class="filter-label">Filter by:</div>
  <div class="filter-select" style="top:93px">Application<svg width="11" height="7"><path d="M1 1l4.5 4.5L10 1" fill="none" stroke="#222" stroke-width="1.8"/></svg></div>
  <div class="filter-select" style="top:135px">Fabric Type<svg width="11" height="7"><path d="M1 1l4.5 4.5L10 1" fill="none" stroke="#222" stroke-width="1.8"/></svg></div>
  <div class="filter-select" style="top:178px">Compatibility<svg width="11" height="7"><path d="M1 1l4.5 4.5L10 1" fill="none" stroke="#222" stroke-width="1.8"/></svg></div>
  <div class="filter-select" style="top:219px">Width<svg width="11" height="7"><path d="M1 1l4.5 4.5L10 1" fill="none" stroke="#222" stroke-width="1.8"/></svg></div>
  <div class="filter-submit">SEARCH</div>
</aside>

<div class="abs hero" role="img" aria-label="Photo inside a greenhouse tunnel with rows of green crops under arched frames"></div>
<div class="abs hero-arrow" style="left:793px"><svg width="12" height="16"><path d="M9 2L3 8l6 6" fill="none" stroke="#fff" stroke-width="2.5"/></svg></div>
<div class="abs hero-arrow" style="left:827px"><svg width="12" height="16"><path d="M3 2l6 6-6 6" fill="none" stroke="#fff" stroke-width="2.5"/></svg></div>

<h2 class="abs section-title">FEATURED PRODUCTS</h2>
<div class="abs pager" style="left:833px"><svg width="8" height="10"><path d="M6 1L2 5l4 4" fill="none" stroke="#fff" stroke-width="1.3"/></svg></div>
<div class="abs pager" style="left:858px"><svg width="8" height="10"><path d="M2 1l4 4-4 4" fill="none" stroke="#fff" stroke-width="1.3"/></svg></div>

<section>
  <div class="abs product-card" style="left:68px;top:564px"><div class="product-photo" role="img" aria-label="Outdoor lounge furniture set" style="background:linear-gradient(#ece8e4,#8a7d74)"></div><div class="product-name" style="top:124px">Outdoor<br>Furniture</div><div class="add-cart">Add to cart</div></div>
  <div class="abs product-card" style="left:210px;top:564px"><div class="product-photo" role="img" aria-label="Green travel backpack" style="background:linear-gradient(#dfe5d4,#6e7d3a)"></div><div class="product-name" style="top:128px">Travel<br>bags</div><div class="add-cart">Add to cart</div></div>
  <div class="abs product-card" style="left:350px;top:564px"><div class="product-photo" role="img" aria-label="Blue dome tent" style="background:linear-gradient(#e8edf5,#3a62b0)"></div><div class="product-name" style="top:136px">Dome Tents</div><div class="add-cart">Add to cart</div></div>
  <div class="abs product-card" style="left:487px;top:564px"><div class="product-photo" role="img" aria-label="Stainless steel barbecue" style="background:linear-gradient(#eeeeee,#a9a9a9)"></div><div class="product-name" style="top:136px">BBQ</div><div class="add-cart">Add to cart</div></div>
  <div class="abs product-card" style="left:627px;top:564px"><div class="product-photo" role="img" aria-label="Canvas cabin tent" style="background:linear-gradient(#ece6dc,#6d5a3c)"></div><div class="product-name" style="top:128px">Canvas<br>Tents</div><div class="add-cart">Add to cart</div></div>
  <div class="abs product-card" style="left:763px;top:564px"><div class="product-photo" role="img" aria-label="Gazebo with screen room walls" style="background:linear-gradient(#2b3d68,#dfe3ea)"></div><div class="product-name" style="top:125px">Gazebos/Scre<br>en Rooms</div><div class="add-cart">Add to cart</div></div>

  <div class="abs product-card" style="left:68px;top:789px"><div class="product-photo" role="img" aria-label="Black outdoor dining table with chairs" style="background:linear-gradient(#eeeeee,#444)"></div><div class="product-name" style="top:124px">Outdoor<br>Furniture</div><div class="add-cart">Add to cart</div></div>
  <div class="abs product-card" style="left:210px;top:789px"><div class="product-photo" role="img" aria-label="Hooded gas barbecue on trolley" style="background:linear-gradient(#e6e6e6,#3c3c3c)"></div><div class="product-name" style="top:128px">Travel<br>bags</div><div class="add-cart">Add to cart</div></div>
  <div class="abs product-card" style="left:350px;top:789px"><div class="product-photo" role="img" aria-label="Folding camp chair" style="background:linear-gradient(#e5eaf0,#2c4a78)"></div><div class="product-name" style="top:136px">Dome Tents</div><div class="add-cart">Add to cart</div></div>
  <div class="abs product-card" style="left:487px;top:789px"><div class="product-photo" role="img" aria-label="Blue hiking backpack" style="background:linear-gradient(#e4e8f2,#2f3f8f)"></div><div class="product-name" style="top:136px">BBQ</div><div class="add-cart">Add to cart</div></div>
  <div class="abs product-card" style="left:627px;top:789px"><div class="product-photo" role="img" aria-label="Folding camp bed" style="background:linear-gradient(#eeeae6,#8a6a5a)"></div><div class="product-name" style="top:128px">Canvas<br>Tents</div><div class="add-cart">Add to cart</div></div>
  <div class="abs product-card" style="left:763px;top:789px"><div class="product-photo" role="img" aria-label="Outdoor corner lounge with cushions" style="background:linear-gradient(#ebebeb,#4a4d55)"></div><div class="product-name" style="top:125px">Gazebos/Scre<br>en Rooms</div><div class="add-cart">Add to cart</div></div>
</section>

<div class="abs contact-tab"><span>Contact us</span></div>

<footer class="abs site-footer">
  <div class="footer-links"><span>HOME</span><span>ABOUT US</span><span>FAQ</span><span>SHIPPING &amp; DELIVERY</span><span>PRIVACY POLICY</span><span>CONTACT US</span></div>
  <div class="footer-social"><i></i><i></i><i></i><i></i><i></i></div>
  <div class="copyright">COPYRIGHT 2014- BRISK LOOM AND CANOPY</div>
</footer>
</body>
</html>
```